Custom Flooring Website For Tulsa Oklahoma Flooring Store

We need to a design for a website that is in between these two current designs, with a modern look and feel.

https://www.talvenfloors.com/
https://mirelopaving.ca/
We need a home page and 2 interior page styles designed.

Talven Flooring is a locally owned flooring company based in Tulsa, Oklahoma. The website should reflect a professional, established business that sells high-quality flooring products, provides expert installation, and specializes in hardwood floor refinishing. The goal of the site is to clearly communicate trust, craftsmanship, and ease of doing business, while guiding users toward visiting the showroom or requesting service.

The company operates a physical showroom in Tulsa where customers can browse flooring materials in person. Talven Flooring sells five primary product categories: solid hardwood, engineered hardwood, laminate, luxury vinyl plank (LVP), and tile. Tile includes both wall and floor applications, as well as decorative options such as glass tile, metal tile, and natural stone. In addition to product sales, the company offers professional flooring installation, hardwood floor refinishing, and water damage restoration related to flooring.

The website structure is intentionally segmented into three main areas: product pages, service pages, and informational pages (About, Financing, Homepage). Product pages focus on education and selection, helping users understand differences between materials and where they work best. Service pages use a more process-driven layout that explains what to expect before, during, and after work is performed. The homepage serves as an overview, positioning Talven Flooring as a full-service flooring store, tile store, and contractor serving Tulsa and surrounding areas.

Visually, the site should feel clean, approachable, and confidence-inspiring—never flashy or overly sales-driven. The design should support browsing materials, understanding services, and contacting the company easily. Strong emphasis should be placed on clear navigation, readable typography, and a layout that works equally well on desktop and mobile devices.

Calls to action should focus on visiting the showroom, scheduling consultations, and exploring flooring options. The financing page should feel simple and reassuring, reducing friction for users considering larger projects. Overall, the design should reflect a business that values craftsmanship, transparency, and long-term relationships with its customers.

Target Market(s)

Retail Flooring Customers who purchase Hardwood, Engineered, Laminate, Vinyl & Tile. Not carpet

Industry/Entity Type

Flooring Store

Number of Pages Required

3 page

Font styles to use
Sans Serif

Colors

Designer to choose colors to be used in the design.

Requirements
Must have
• We like these two designs (Home Pages) https://www.talvenfloors.com/ https://mirelopaving.ca/
Nice to have
• We need a home page and two interior pages. The website will have 20+ pages coded by our developer, but we will use one home page design and 2 alternating interior pages to fill the website.

```html
<!DOCTYPE html>
<html lang="en">
<head>
<meta charset="utf-8">
<title>Talven Flooring — Tulsa Flooring Store</title>
<link href="https://fonts.googleapis.com/css2?family=Righteous&family=Montserrat:wght@400;500;600&display=swap" rel="stylesheet">
<style>
:root{
  --red:#93062a;
  --red-dark:#7a0522;
  --ink:#1f1f1f;
  --text:#4a4a4a;
  --gray-bg:#ebebeb;
  --dark:#2b2b2b;
  --header:rgba(30,30,30,.82);
  --white:#ffffff;
  --mark:#c24a22;
}
*{margin:0;padding:0;box-sizing:border-box}
html,body{width:1200px;height:4819px;overflow:hidden}
body{position:relative;font-family:"Montserrat",sans-serif;color:var(--text);background:var(--white)}
.display{font-family:"Righteous",sans-serif;color:var(--ink);font-weight:400}
.abs{position:absolute}
.btn{position:absolute;display:flex;align-items:center;justify-content:center;height:40px;padding:0 18px;font-size:14px;font-weight:500;color:var(--white);background:var(--red);text-decoration:none}
.btn-outline{background:transparent;border:1px solid rgba(255,255,255,.8)}
.mark{position:absolute;width:34px;height:34px;background:var(--mark)}
.rule{position:absolute;height:2px;background:var(--red)}
.photo{position:absolute}

/* header */
.site-header{position:absolute;left:0;top:0;width:1200px;height:94px;background:var(--header);z-index:3}
.brand{position:absolute;left:56px;top:28px;display:flex;align-items:center;gap:10px;font-family:"Righteous",sans-serif;font-size:30px;color:var(--white);text-decoration:none}
.brand-square{width:14px;height:14px;background:var(--mark)}
.main-nav{position:absolute;right:54px;top:36px;display:flex;gap:29px}
.main-nav a{font-family:"Righteous",sans-serif;font-size:15px;color:var(--white);text-decoration:none}
.main-nav a.current{text-decoration:underline;text-underline-offset:4px}

/* hero */
.hero{position:absolute;left:0;top:0;width:1200px;height:618px;background:linear-gradient(100deg,#5a5450 0%,#8c857e 45%,#b7aea4 70%,#6e6660 100%)}
.hero-shade{position:absolute;inset:0;background:linear-gradient(90deg,rgba(0,0,0,.45),rgba(0,0,0,.05) 70%)}
.hero h1{position:absolute;left:54px;top:212px;width:760px;font-family:"Righteous",sans-serif;font-weight:400;font-size:42px;line-height:51px;color:var(--white)}
.hero p{position:absolute;left:54px;top:400px;width:760px;font-size:14.5px;line-height:24px;color:var(--white)}

/* product cards */
.product-card{position:absolute;top:914px;width:221px;height:293px;border:1px solid #777;background:#e2e2e2}
.product-card .photo{left:0;top:0;width:219px;height:239px}
.product-card span{position:absolute;left:0;bottom:0;width:100%;height:53px;display:flex;align-items:center;justify-content:center;font-family:"Righteous",sans-serif;font-size:16px;color:var(--ink)}

/* about */
.section-copy{font-size:14.5px;line-height:25.5px;color:var(--text)}
.dots{position:absolute;display:grid;gap:9px}
.dots i{display:block;width:3px;height:3px;background:var(--white);border-radius:50%}

/* services */
.service-card{position:absolute;top:2390px;width:300px;height:291px}
.service-card .photo{inset:0}
.service-tag{position:absolute;left:40px;bottom:-12px;width:222px;height:36px;background:#1a1a1a;color:var(--white);font-family:"Righteous",sans-serif;font-size:17px;display:flex;align-items:center;justify-content:center}
.service-tag:before,.service-tag:after{content:"";position:absolute;bottom:-8px;border-top:8px solid #1a1a1a}
.service-tag:before{left:0;border-left:12px solid transparent}
.service-tag:after{right:0;border-right:12px solid transparent}
.arrow-btn{position:absolute;top:2719px;width:38px;height:38px;border-radius:50%;display:flex;align-items:center;justify-content:center}

/* features */
.feature{position:absolute;width:440px;height:100px}
.feature-icon{position:absolute;left:0;top:0;width:94px;height:94px}
.feature h3{position:absolute;left:120px;top:0;font-family:"Righteous",sans-serif;font-weight:400;font-size:17px;line-height:20px;color:var(--ink)}
.feature p{position:absolute;left:120px;top:46px;width:290px;font-size:12px;line-height:19px;color:#777;text-align:justify}

/* footer */
.site-footer{position:absolute;left:0;top:4616px;width:1200px;height:203px;background:var(--dark)}
.footer-nav{position:absolute;right:130px;top:70px;width:480px;display:flex;flex-wrap:wrap;justify-content:flex-end;column-gap:28px;row-gap:4px}
.footer-nav a{font-family:"Righteous",sans-serif;font-size:15px;color:var(--white);text-decoration:none}
.copyright{position:absolute;left:0;width:100%;top:168px;text-align:center;font-family:"Righteous",sans-serif;font-size:10px;color:var(--white)}
</style>
</head>
<body>

<!-- Header -->
<header class="site-header">
  <a class="brand" href="https://www.talvenfloors.com/">Talven Flooring<span class="brand-square"></span></a>
  <nav class="main-nav">
    <a class="current" href="#">Home</a><a href="#">Products</a><a href="#">Services</a><a href="#">Reviews</a><a href="#">Financing</a><a href="#">Inspiration</a><a href="#">About us</a><a href="#">Contact</a>
  </nav>
</header>

<!-- Hero -->
<section class="hero">
  <div class="photo" style="inset:0" role="img" aria-label="Bright modern interior with wood floors and an open staircase with metal railings"></div>
  <div class="hero-shade"></div>
  <h1>Tulsa’s Local Flooring Store for Quality Materials &amp; Expert Installation</h1>
  <p>Talven Flooring is a locally owned flooring store in Tulsa offering high-quality flooring products, professional installation, and hardwood floor refinishing—all from one trusted team.</p>
  <a class="btn" style="left:54px;top:465px;width:182px">Visit Our Showroom</a>
  <a class="btn btn-outline" style="left:249px;top:465px;width:216px">Explore Flooring Options</a>
</section>

<!-- Products -->
<section>
  <div class="mark" style="left:583px;top:723px"></div>
  <h2 class="display abs" style="left:0;width:1200px;top:790px;text-align:center;font-size:37px">Flooring Products for Every Space</h2>
  <div class="rule" style="left:454px;top:855px;width:292px"></div>
  <div class="product-card" style="left:110px"><div class="photo" style="background:linear-gradient(160deg,#b59a7c,#8a6a4c)" role="img" aria-label="Dining room with solid hardwood floor"></div><span>Solid Hardwood</span></div>
  <div class="product-card" style="left:363px"><div class="photo" style="background:linear-gradient(160deg,#7a5a40,#4e3424)" role="img" aria-label="Living room with engineered hardwood floor"></div><span>Engineered Hardwood</span></div>
  <div class="product-card" style="left:616px"><div class="photo" style="background:linear-gradient(180deg,#3d4468 0%,#5a5f7e 35%,#d8d2c6 36%,#c9c2b4 100%)" role="img" aria-label="Kitchen with navy cabinets and stone-look laminate floor"></div><span>Laminate Flooring</span></div>
  <div class="product-card" style="left:869px"><div class="photo" style="background:linear-gradient(160deg,#eceae6,#c9c5be 60%,#4a3a32)" role="img" aria-label="Bathroom with large marble tile floor and dark vanity"></div><span>Tile</span></div>
  <a class="btn" style="left:482px;top:1246px;width:236px">View All Flooring Products</a>
</section>

<!-- About -->
<section>
  <div class="mark" style="left:120px;top:1402px"></div>
  <h2 class="display abs" style="left:110px;top:1470px;width:480px;font-size:37px;line-height:44px">A Trusted Flooring Store Serving Tulsa</h2>
  <div class="rule" style="left:110px;top:1577px;width:136px"></div>
  <p class="section-copy abs" style="left:110px;top:1610px;width:474px;text-align:justify">From our Tulsa showroom, we help homeowners and contractors choose flooring that fits their space, lifestyle, and budget—then install it with care &amp; precision. Whether you’re building, remodeling, or restoring existing floors, we provide straightforward guidance, skilled workmanship, and results that last.</p>
  <a class="btn" style="left:110px;top:1777px;width:124px">About Us</a>
  <div class="abs" style="left:973px;top:1372px;width:227px;height:532px;background:var(--red)"></div>
  <div class="abs" style="left:628px;top:1446px;width:472px;height:384px;background:var(--white);box-shadow:0 2px 6px rgba(0,0,0,.15)"></div>
  <div class="photo" style="left:640px;top:1458px;width:448px;height:360px;background:linear-gradient(180deg,#e8e4de 0%,#d9d3ca 45%,#4d4a47 60%,#38363a 100%)" role="img" aria-label="Living room with white sofas, fireplace and dark plank floor"></div>
  <div class="dots" style="left:1114px;top:1762px;grid-template-columns:3px 3px"><i></i><i></i><i></i><i></i><i></i><i></i><i></i><i></i><i></i><i></i></div>
  <div class="dots" style="left:1032px;top:1858px;grid-template-columns:repeat(8,3px)"><i></i><i></i><i></i><i></i><i></i><i></i><i></i><i></i></div>
</section>

<!-- Services -->
<section class="abs" style="left:0;top:1990px;width:1200px;height:855px;background:var(--gray-bg)"></section>
<section>
  <div class="mark" style="left:583px;top:2102px"></div>
  <h2 class="display abs" style="left:0;width:1200px;top:2167px;text-align:center;font-size:37px;line-height:44px">Professional<br>Installation &amp; Refinishing Services</h2>
  <div class="rule" style="left:494px;top:2275px;width:212px"></div>
  <p class="abs" style="left:150px;width:900px;top:2306px;text-align:center;font-size:14px;line-height:24px">In addition to selling flooring, Talven Flooring provides expert installation and refinishing services. Our experienced team handles projects of all sizes with attention to detail and clear communication from start to finish.</p>
  <div class="service-card" style="left:110px"><div class="photo" style="background:linear-gradient(160deg,#a49c92,#6a6058)" role="img" aria-label="Installer laying floor planks"></div><div class="service-tag">Flooring Installation</div></div>
  <div class="service-card" style="left:449px"><div class="photo" style="background:linear-gradient(180deg,#8a7f74,#b88b5a 60%,#8a5a30)" role="img" aria-label="Floor sanding machine on hardwood"></div><div class="service-tag">Floor Refinishing</div></div>
  <div class="service-card" style="left:788px"><div class="photo" style="background:linear-gradient(170deg,#9a8a78,#7a4a28 60%,#5a3018)" role="img" aria-label="Water pooled on a glossy wood floor"></div><div class="service-tag">Water Damage</div></div>
  <div class="arrow-btn" style="left:556px;border:1.5px solid var(--red)"><svg width="12" height="12" viewBox="0 0 12 12"><path d="M8 1 3 6l5 5" fill="none" stroke="#93062a" stroke-width="2"/></svg></div>
  <div class="arrow-btn" style="left:606px;background:var(--red)"><svg width="12" height="12" viewBox="0 0 12 12"><path d="M4 1l5 5-5 5" fill="none" stroke="#fff" stroke-width="2"/></svg></div>
</section>

<!-- Why us -->
<section>
  <div class="mark" style="left:138px;top:2954px"></div>
  <h2 class="display abs" style="left:110px;top:3018px;font-size:37px">More Than a Flooring Store</h2>
  <div class="rule" style="left:110px;top:3077px;width:136px"></div>
  <p class="abs" style="left:110px;top:3118px;width:990px;font-size:14px;line-height:25px">What sets Talven Flooring apart is experience and craftsmanship. We work closely with homeowners and contractors to ensure every project is done correctly, from subfloor preparation to final trim details.</p>
  <div class="abs" style="left:599px;top:3224px;width:2px;height:192px;background:var(--red)"></div>

  <div class="feature" style="left:118px;top:3207px">
    <svg class="feature-icon" viewBox="0 0 94 94"><rect x="19" y="19" width="56" height="56" transform="rotate(45 47 47)" fill="#dedede"/><path d="M47 33 63 47 47 61 31 47Z" fill="#93062a"/><path d="M36 47h22" stroke="#fff" stroke-width="2"/></svg>
    <h3>Local<br>Tulsa Showroom</h3>
    <p>Lorem ipsum dolor sit amet, consectetur adipiscing elit, sed do</p>
  </div>
  <div class="feature" style="left:118px;top:3332px">
    <svg class="feature-icon" viewBox="0 0 94 94"><rect x="19" y="19" width="56" height="56" transform="rotate(45 47 47)" fill="#dedede"/><rect x="35" y="34" width="24" height="26" fill="#93062a"/><path d="M35 43h24M47 34v26" stroke="#dedede" stroke-width="2"/></svg>
    <h3>Skilled Installers &amp;<br>Finishers</h3>
    <p>Lorem ipsum dolor sit amet, consectetur adipiscing elit, sed do</p>
  </div>
  <div class="feature" style="left:678px;top:3207px">
    <svg class="feature-icon" viewBox="0 0 94 94"><rect x="19" y="19" width="56" height="56" transform="rotate(45 47 47)" fill="#dedede"/><rect x="33" y="35" width="10" height="10" fill="#93062a"/><rect x="45" y="35" width="10" height="10" fill="#93062a"/><rect x="33" y="47" width="10" height="10" fill="#93062a"/><rect x="45" y="47" width="10" height="10" fill="#93062a"/><path d="M60 34v24" stroke="#93062a" stroke-width="3"/></svg>
    <h3>Honest Recommendations —<br>No Pressure</h3>
    <p>Lorem ipsum dolor sit amet, consectetur adipiscing elit, sed do</p>
  </div>
  <div class="feature" style="left:678px;top:3332px">
    <svg class="feature-icon" viewBox="0 0 94 94"><rect x="19" y="19" width="56" height="56" transform="rotate(45 47 47)" fill="#dedede"/><circle cx="49" cy="48" r="12" fill="none" stroke="#93062a" stroke-width="3"/><path d="M49 41v7l5 3" fill="none" stroke="#93062a" stroke-width="2.5"/><path d="M34 46l4 4 5-6" fill="none" stroke="#93062a" stroke-width="2.5"/></svg>
    <h3>Products Selected for<br>Long-Term Performance</h3>
    <p>Lorem ipsum dolor sit amet, consectetur adipiscing elit, sed do</p>
  </div>
</section>

<!-- Showroom -->
<section>
  <div class="abs" style="left:0;top:3516px;width:227px;height:533px;background:var(--red)"></div>
  <div class="photo" style="left:110px;top:3604px;width:448px;height:357px;background:linear-gradient(180deg,#e8e4de 0%,#d9d3ca 45%,#4d4a47 60%,#38363a 100%)" role="img" aria-label="Showroom living space with white sofas, fireplace and dark plank floor"></div>
  <div class="dots" style="left:66px;top:3906px;grid-template-columns:3px 3px"><i></i><i></i><i></i><i></i><i></i><i></i><i></i><i></i></div>
  <div class="dots" style="left:66px;top:3994px;grid-template-columns:repeat(8,3px)"><i></i><i></i><i></i><i></i><i></i><i></i><i></i><i></i></div>
  <div class="mark" style="left:641px;top:3581px"></div>
  <h2 class="display abs" style="left:614px;top:3651px;width:480px;font-size:37px;line-height:44px">Visit Our Tulsa Showroom</h2>
  <div class="rule" style="left:614px;top:3754px;width:110px"></div>
  <p class="abs" style="left:614px;top:3790px;width:496px;font-size:13px;line-height:25.5px;text-align:justify">Choosing flooring online only goes so far. Seeing materials in person makes a real difference. We invite you to visit the Talven Flooring showroom in Tulsa, where you can explore hardwood, LVP, laminate, and tile options—including wall tile and floor tile—side by side.</p>
  <p class="abs" style="left:614px;top:3900px;width:496px;font-size:13px;line-height:25.5px;text-align:justify">Our team is happy to answer questions, explain differences between materials, and help you plan your next project.</p>
  <a class="btn" style="left:614px;top:3966px;width:134px">Get Directions</a>
</section>

<!-- Service area -->
<section class="abs" style="left:0;top:4133px;width:1200px;height:483px;background:var(--gray-bg)">
  <div class="mark" style="left:583px;top:96px"></div>
  <h2 class="display abs" style="left:0;width:1200px;top:164px;text-align:center;font-size:37px">Serving Tulsa &amp; Surrounding Areas</h2>
  <div class="rule" style="left:540px;top:258px;width:120px"></div>
  <p class="abs" style="left:200px;width:800px;top:278px;text-align:center;font-size:14px;line-height:25px">Talven Flooring proudly serves Tulsa and nearby communities with reliable flooring products and professional service. Whether you’re updating a single room or planning a full renovation, we’re here to help from start to finish.</p>
  <a class="btn" style="left:490px;top:368px;width:220px">Schedule a Consultation</a>
</section>

<!-- Footer -->
<footer class="site-footer">
  <a class="brand" href="https://www.talvenfloors.com/" style="left:110px;top:66px">Talven Flooring<span class="brand-square"></span></a>
  <nav class="footer-nav">
    <a href="#">Home</a><a href="#">Products</a><a href="#">Services</a><a href="#">Reviews</a><a href="#">Financing</a><a href="#">Inspiration</a><a href="#">About us</a><a href="#">Contact</a>
  </nav>
  <p class="copyright">Copyright © 2026 Talven Flooring Co. | Privacy | Accessibility</p>
</footer>

</body>
</html>
```